Medical Internet Marketing Company Needs a Site!

We need a new, fresh website for our search engine optimization and social media marketing company. We specialize in helping medical practices, doctors, physicians, and hospitals with their online presence and web ranking. The site should lean towards being suited for these audiences.

We have several examples of website that we like as well as things that we like about them.

Here are sites that we enjoy.

www.brightwavelab.com

It's a good design for the site all around. The videos, buttons, and images are all excellent. They did a fine job.

- We really like their "contact us" side bar and want to include one like it on the secondary pages.

www.corvantis.net

- We don't like the "thickness" of the top navigation bar.
- We like the page colors, easy navigation, and big call to action phone number in the top right corner.

http://www.teluvo.com/

Out of all the examples provided, Teluvo is our favorite and closest look and style to what we are looking for.

- We really like the openness of the design, such as space between the text and background.

- We want a price page in a style very similar to their pricing page with the services listed and check-marks, etc. although we intend to have multiple service package columns much like Corvantis's SEO pricing page.

- The way the video fits into the home page header is very organized, simple, and attention grabbing. We intend to place a slider with videos here.

- We need a page design that will allow for an image slider like Teluvo's Features page.

Here's a great example of a medical internet marketing website: http://www.dermaplex.com/

Target Market(s)

Our target market is doctors, typically male and typically 40-45 years old. I

Industry/Entity Type

Marketing

Requirements
Must have
• The homepage should have a slider in the video. Interior pages should have a video in the very top similar to how they do it on www.brightwavelab.com

The top navigation tabs needed are:
- Home
- Solutions
- Resources
- About
- Why Quelvo
- Contact

The sidebar should have a GREAT call to action in it on interior pages.

There should be one interior page that is similar to this - http://www.teluvo.com/pricing/

There needs to be a page with multiple boxes that take up a row of the web page's body. This page will house all the case studies similar to brightwave lab's: http://www.brightwavelab.com/success-stories/case-studies/ The one exception is we want the case studies to be inside of "boxes" instead of between horizontal lines like brightwave lab's.
Nice to have
• Color, professional, and clean. GREAT use of calls to actions.

```html
<!DOCTYPE html>
<html lang="en">
<head>
<meta charset="utf-8">
<title>Quelvo – Medical Internet Marketing</title>
<link rel="stylesheet" href="https://fonts.googleapis.com/css2?family=Open+Sans:wght@400;600;700&display=swap">
<style>
  :root {
    --navy: #0d2a55;
    --navy-deep: #0a2347;
    --ink: #1f1f1f;
    --grey-text: #555b63;
    --grey-panel: #e4e4e4;
    --grey-strip: #6a6a6a;
    --white: #ffffff;
    --tint-blue: rgba(120, 190, 235, 0.28);
    --tint-green: rgba(140, 195, 90, 0.30);
    --tint-orange: rgba(250, 175, 110, 0.28);
    --brand-red: #d3262b;
    --brand-teal: #2a7f9a;
    --brand-olive: #5b7a2a;
    --brand-blue: #1d5fa8;
  }
  * { box-sizing: border-box; margin: 0; padding: 0; }
  html, body { width: 1200px; height: 1200px; overflow: hidden; }
  body {
    position: relative;
    font-family: "Open Sans", sans-serif;
    color: var(--ink);
    background:
      radial-gradient(ellipse 420px 700px at 1150px 300px, var(--tint-blue), transparent 70%),
      radial-gradient(ellipse 520px 480px at 800px 900px, var(--tint-green), transparent 70%),
      radial-gradient(ellipse 520px 420px at 120px 980px, var(--tint-orange), transparent 70%),
      var(--white);
  }

  /* Header */
  .site-header { position: absolute; left: 0; top: 0; width: 1200px; height: 126px; }
  .brand { position: absolute; left: 65px; top: 50px; display: flex; align-items: center; gap: 14px; }
  .brand-square { width: 46px; height: 46px; background: var(--navy); }
  .brand-name { font-size: 56px; font-weight: 600; color: #7a7a7a; letter-spacing: 4px; line-height: 1; }
  .phone-cta {
    position: absolute; left: 862px; top: 22px; height: 58px; width: 276px;
    display: flex; align-items: center;
  }
  .phone-cta .phone-circle {
    width: 58px; height: 58px; border-radius: 50%; background: var(--navy);
    display: flex; align-items: center; justify-content: center; position: relative; z-index: 2;
  }
  .phone-cta .phone-number {
    margin-left: -12px; height: 40px; flex: 1; background: var(--navy); color: var(--white);
    font-size: 30px; font-weight: 400; display: flex; align-items: center; padding-left: 26px;
  }
  .main-nav { position: absolute; right: 62px; top: 95px; display: flex; gap: 32px; }
  .main-nav a { font-size: 19px; font-weight: 700; color: var(--ink); text-decoration: none; }
  .header-rule { position: absolute; left: 35px; top: 125px; width: 1127px; height: 2px; background: #555; }

  /* Hero */
  .hero {
    position: absolute; left: 35px; top: 127px; width: 1127px; height: 378px;
    background: radial-gradient(ellipse at 40% 45%, #ffffff 0%, #f2f2f2 45%, #d6d6d6 100%);
  }
  .hero-strip { position: absolute; left: 35px; top: 492px; width: 1127px; height: 13px; background: var(--grey-strip); }
  .hero-intro { position: absolute; left: 70px; top: 188px; width: 445px; text-align: center; }
  .hero-mark { width: 48px; height: 40px; background: var(--navy); margin: 0 auto 12px; }
  .hero-title { font-size: 27px; font-weight: 400; color: var(--navy); line-height: 33px; letter-spacing: 0.3px; }
  .hero-lede { margin-top: 10px; font-size: 19px; color: var(--grey-text); line-height: 23px; }
  .speciality-ribbon { position: absolute; left: 30px; top: 397px; }
  .speciality-ribbon span {
    position: absolute; left: 44px; top: 8px; color: var(--white); font-size: 23px; font-weight: 400;
  }
  .speciality-tabs { position: absolute; left: 44px; top: 518px; display: flex; gap: 8px; }
  .speciality-tabs a {
    width: 113px; height: 44px; background: var(--navy); color: var(--white);
    font-size: 10.5px; font-weight: 600; text-decoration: none; text-transform: uppercase;
    display: flex; align-items: center; justify-content: center;
    box-shadow: 0 6px 6px -3px rgba(0,0,0,0.25);
  }
  .video-frame {
    position: absolute; left: 542px; top: 180px; width: 571px; height: 392px;
    background: var(--white); padding: 10px; box-shadow: 0 4px 16px rgba(0,0,0,0.35);
  }
  .video-screen {
    width: 100%; height: 100%;
    background: radial-gradient(ellipse at 50% 45%, #133a6e 0%, #0b2a55 60%, #082146 100%);
    position: relative; text-align: center; color: var(--white);
  }
  .video-screen svg { position: absolute; left: 220px; top: 118px; }
  .video-label { position: absolute; left: 0; right: 0; top: 248px; }
  .video-label strong { display: block; font-size: 22px; font-weight: 700; }
  .video-label small { display: block; font-size: 15px; margin-left: 80px; }

  /* Intro */
  .intro {
    position: absolute; left: 60px; top: 626px; width: 1080px; text-align: center;
    font-size: 15px; line-height: 19px; color: #4a4a4a;
  }
  .intro strong { color: #333; font-size: 16px; }

  /* Panels */
  .panel {
    position: absolute; top: 722px; width: 552px; height: 326px;
    background: rgba(255,255,255,0.55); border: 1px solid #dcdcdc;
    box-shadow: inset 0 30px 40px -20px rgba(0,0,0,0.08);
  }
  .panel-stories { left: 35px; }
  .panel-clients { left: 610px; }
  .panel-title {
    text-align: center; font-size: 30px; font-weight: 400; color: var(--navy);
    margin-top: 42px; line-height: 36px;
  }
  .story-quote {
    margin: 16px 20px 0 20px; font-size: 15px; line-height: 18.7px; color: #3d3d3d;
    text-align: justify; letter-spacing: 0.3px;
  }
  .story-author { margin: 18px 20px 0; font-size: 15px; color: #3d3d3d; }
  .panel-link {
    position: absolute; bottom: 20px; font-size: 15px; font-weight: 700; color: var(--navy);
    text-decoration: none; letter-spacing: 0.5px;
  }
  .panel-stories .panel-link { right: 28px; }
  .panel-clients .panel-link { right: 28px; }
  .clients-lede { text-align: center; font-size: 16px; color: #444; line-height: 20px; margin-top: 6px; }
  .client-grid {
    display: grid; grid-template-columns: 1fr 1fr; row-gap: 30px; margin: 34px 40px 0;
  }
  .client { display: flex; align-items: center; justify-content: center; gap: 8px; font-size: 30px; font-weight: 600; }
  .client-dot { width: 14px; height: 14px; border-radius: 50%; }

  /* Footer */
  .site-footer {
    position: absolute; left: 35px; top: 1075px; width: 1127px; height: 125px; background: var(--navy);
    color: var(--white);
  }
  .footer-brand { position: absolute; left: 24px; top: 16px; display: flex; align-items: center; gap: 12px; }
  .footer-brand .brand-square { width: 38px; height: 38px; background: var(--white); }
  .footer-brand .brand-name { font-size: 46px; color: #c9ccd2; }
  .footer-nav { position: absolute; left: 24px; top: 62px; font-size: 18px; }
  .footer-nav a { color: var(--white); text-decoration: none; }
  .footer-nav .sep { margin: 0 7px; }
  .copyright { position: absolute; left: 24px; top: 96px; font-size: 14px; }
  .social-title { position: absolute; right: 30px; top: 26px; font-size: 18px; font-weight: 700; }
  .social-list { position: absolute; right: 28px; top: 54px; display: flex; gap: 6px; }
  .social-list a {
    width: 50px; height: 50px; border-radius: 8px; background: #ffffff;
    color: var(--navy); font-size: 9px; font-weight: 600; text-decoration: none;
    display: flex; align-items: center; justify-content: center;
  }
</style>
</head>
<body>
  <header class="site-header">
    <div class="brand">
      <span class="brand-square"></span>
      <span class="brand-name">QUELVO</span>
    </div>
    <div class="phone-cta">
      <span class="phone-circle">
        <svg width="30" height="34" viewBox="0 0 30 34" aria-hidden="true">
          <path d="M7 2 L12 2 L13 10 L9 12 Q11 20 17 25 L20 22 L27 24 L27 30 Q22 33 16 29 Q5 21 4 8 Q4 4 7 2 Z" fill="#fff"/>
        </svg>
      </span>
      <span class="phone-number">123-456-7890</span>
    </div>
    <nav class="main-nav">
      <a href="#">Home</a>
      <a href="#">Solutions</a>
      <a href="#">Resources</a>
      <a href="#">About</a>
      <a href="#">Why Quelvo</a>
      <a href="#">Contact</a>
    </nav>
    <div class="header-rule"></div>
  </header>

  <section class="hero"></section>
  <div class="hero-strip"></div>

  <div class="hero-intro">
    <div class="hero-mark"></div>
    <h1 class="hero-title">MEDICAL INTERNET MARKETING<br>THAT GET RESULTS</h1>
    <p class="hero-lede">We specialize in helping medical practices, doctors, physicians, and hospitals with their online presence and web ranking</p>
  </div>

  <div class="speciality-ribbon">
    <svg width="382" height="50" viewBox="0 0 382 50" aria-hidden="true">
      <polygon points="0,4 382,4 346,46 0,46" fill="#0d2a55"/>
      <polygon points="0,46 346,46 340,50 0,50" fill="#9aa3ad"/>
    </svg>
    <span>Select Your Speciality !</span>
  </div>

  <nav class="speciality-tabs">
    <a href="#">Medical Practices</a>
    <a href="#">Doctors</a>
    <a href="#">Physicians</a>
    <a href="#">Hospitals</a>
  </nav>

  <div class="video-frame">
    <div class="video-screen">
      <svg width="122" height="122" viewBox="0 0 122 122" aria-hidden="true">
        <circle cx="61" cy="61" r="58" fill="none" stroke="#fff" stroke-width="3"/>
        <polygon points="45,35 45,87 88,61" fill="#fff"/>
      </svg>
      <div class="video-label">
        <strong>HOW IT WORKS</strong>
        <small>90 Sec Tutorial</small>
      </div>
    </div>
  </div>

  <p class="intro"><strong>QUELVO</strong> is the world's leading provider of websites and online medical marketing for healthcare practices. We are recommended by more than 20 highly regarded medical associations and have worked with over 6,000 healthcare providers worldwide. Our medical Internet Marketing services can give you top rankings on Searcha, a strong image for your practice, more patients and more referrals.</p>

  <section class="panel panel-stories">
    <h2 class="panel-title">SUCCESS STORIES...</h2>
    <p class="story-quote">We are very satisfied with the efforts of QUELVO to connect Norvik Home with our valued consumers via our internet marketing initiatives. Their program is affordable and the relationship from the start has been very thorough and easy to implement. Their ongoing support with their creative and responsive staff has been excellent. We have recommended QUELVO with many of our business associates and will continue to do so.</p>
    <p class="story-author">Martin K., VP Marketing, Norvik Appliances</p>
    <a class="panel-link" href="#">READ MORE STORIES !</a>
  </section>

  <section class="panel panel-clients">
    <h2 class="panel-title">OUR CLIENT`S</h2>
    <p class="clients-lede">Some of our clients<br>whom we are working with..</p>
    <div class="client-grid">
      <div class="client" style="color: var(--brand-red);">Carewell</div>
      <div class="client" style="color: var(--brand-teal);">Solvanta</div>
      <div class="client" style="color: var(--brand-olive);"><span class="client-dot" style="background: var(--brand-olive);"></span>Adcrest</div>
      <div class="client" style="color: var(--brand-blue);">Vantor Energy</div>
    </div>
    <a class="panel-link" href="#">SEE MORE !</a>
  </section>

  <footer class="site-footer">
    <div class="footer-brand">
      <span class="brand-square"></span>
      <span class="brand-name">QUELVO</span>
    </div>
    <nav class="footer-nav">
      <a href="#">Home</a><span class="sep">|</span><a href="#">Solutions</a><span class="sep">|</span><a href="#">Resources</a><span class="sep">|</span><a href="#">About</a><span class="sep">|</span><a href="#">Why Quelvo</a><span class="sep">|</span><a href="#">Contact</a>
    </nav>
    <p class="copyright">Copyright © 2012 QUELVO. All rights reserved.</p>
    <p class="social-title">Get Social With Us !</p>
    <nav class="social-list">
      <a href="#">Konnekt</a>
      <a href="#">Chirpa</a>
      <a href="#">Vidora</a>
      <a href="#">Searcha</a>
      <a href="#">Photra</a>
      <a href="#">Feedra</a>
    </nav>
  </footer>
</body>
</html>
```